family chiropractic health care team needs a modern business card design

Healthcare office with Chiropractors, Physiotherapists, Massage therapists and possibly other practitioners in the future. This is a friendly family office with patients of all ages (and lots of kids) that just moved into a new larger modern office.
Look at the website for photos of the office.
Design for the front and back of a business card required.
Text for the front:
Office logo and name of the office:
Bright Path Wellness Centre
Name of current Practitioner:
Dr. Marten Quogue B.Sc., D.C. Chiropractor
(But please include options to swap out name and title for other practitioners )

address:
217 Tamsey Road
Etobicoke ON.
K2R 6P4
Phone: 416-870-2961 (MOVE)
Web site and email:
www.brightpathwellcentre.example
brightpathchiro@mailnest.example

2 versions of the back of the card:
1. text below
2. appointment schedule card

Text on back of card:
Chiropractic Card text on back of the card:
There is more to chiropractic than the relief of headaches and back pain! Our primary focus is the integrity of your nerve system, which controls and regulates every cell and tissue of your body. The moving bones of the spinal column can impair this vital communication link between your brain and body. We help improve the function and structure of your spine, reducing nerve system compromise. The result?
Even non-spinal related health problems can show improvement
without drugs
without surgery
regardless of age
for over a century
naturally

Appointment Card info For Back:
Please integrate design elements from the front of the card into an appointment card format.
M Tu W Th F Sat (and a line for writing on beside each one)

```html
<!DOCTYPE html>
<html lang="en">
<head>
<meta charset="utf-8">
<title>Bright Path Wellness Centre – Business Card</title>
<link href="https://fonts.googleapis.com/css2?family=Arimo:wght@400;700&display=swap" rel="stylesheet">
<style>
  :root {
    --bg: #3a3a3a;
    --green: #97c157;
    --white: #ffffff;
    --grey: #7a7a7a;
    --ink-green: #8dbb45;
  }
  * { margin: 0; padding: 0; box-sizing: border-box; }
  html, body { width: 1200px; height: 689px; overflow: hidden; }
  body {
    background: var(--bg);
    font-family: "Arimo", Arial, sans-serif;
    position: relative;
  }
  .card {
    position: absolute;
    top: 190px;
    width: 540px;
    height: 309px;
    border-radius: 18px;
    overflow: hidden;
  }
  /* Back */
  .card-back {
    left: 30px;
    background: var(--green);
    color: var(--white);
    text-align: center;
    padding: 40px 36px 0;
  }
  .brand-name {
    font-weight: 700;
    font-size: 26px;
    letter-spacing: 1px;
    text-transform: uppercase;
    line-height: 1.1;
  }
  .card-back .brand-name { color: var(--white); }
  .brand-rule {
    display: flex; align-items: center; justify-content: center; gap: 10px;
    margin: 6px auto 0; width: 280px;
  }
  .brand-rule span { flex: 1; height: 1px; background: currentColor; }
  .brand-rule b { font-weight: 400; font-size: 11px; letter-spacing: 10px; }
  .back-copy {
    margin-top: 18px;
    font-size: 10.2px;
    line-height: 1.32;
  }
  .back-lead {
    margin-top: 10px;
    font-size: 13px;
    font-weight: 700;
  }
  .benefits {
    list-style: none;
    margin-top: 4px;
    font-size: 11px;
    line-height: 1.45;
  }
  .benefits li { display: inline-flex; align-items: center; gap: 4px; margin: 0 4px; }
  .tick { width: 10px; height: 10px; }
  /* Front */
  .card-front {
    left: 630px;
    background: var(--white);
  }
  .front-logo {
    position: absolute; top: 58px; left: 0; right: 0;
    text-align: center;
    color: var(--grey);
  }
  .front-logo .brand-name { color: var(--ink-green); font-size: 28px; }
  .front-band {
    position: absolute; left: 0; right: 0; top: 168px; bottom: 0;
    background: var(--green);
    border-top: 6px solid var(--grey);
    color: var(--white);
    display: flex; align-items: center;
    padding: 0 24px;
  }
  .practitioner { width: 230px; text-align: right; padding-right: 16px; }
  .practitioner-name { font-size: 21px; font-weight: 700; }
  .practitioner-cred, .practitioner-title { font-size: 12px; margin-top: 3px; }
  .divider { width: 1px; height: 96px; background: rgba(255,255,255,.8); }
  .contact { padding-left: 16px; font-size: 11.5px; line-height: 1.45; }
  .contact-row { display: flex; align-items: center; gap: 6px; }
  .icon { width: 10px; height: 10px; flex: none; }
</style>
</head>
<body>

<section class="card card-back" aria-label="Card back">
  <div class="brand-name">Bright Path Wellness</div>
  <div class="brand-rule"><span></span><b>CENTRE</b><span></span></div>
  <p class="back-copy">There is more to chiropractic than the relief of headaches and back pain! Our primary focus is the integrity of your nerve system, which controls and regulates every cell and tissue of your body. The moving bones of the spinal column can impair this vital communication link between your brain and body. We help improve the function and structure of your spine, reducing nerve system compromise. The result?</p>
  <p class="back-lead">Even non-spinal related health problems can show improvement</p>
  <ul class="benefits">
    <li><svg class="tick" viewBox="0 0 10 10"><circle cx="5" cy="5" r="5" fill="#fff"/><path d="M2.6 5.2l1.6 1.6 3.2-3.4" stroke="#97c157" stroke-width="1.4" fill="none"/></svg>without drugs</li>
    <li><svg class="tick" viewBox="0 0 10 10"><circle cx="5" cy="5" r="5" fill="#fff"/><path d="M2.6 5.2l1.6 1.6 3.2-3.4" stroke="#97c157" stroke-width="1.4" fill="none"/></svg>without surgery</li>
    <li><svg class="tick" viewBox="0 0 10 10"><circle cx="5" cy="5" r="5" fill="#fff"/><path d="M2.6 5.2l1.6 1.6 3.2-3.4" stroke="#97c157" stroke-width="1.4" fill="none"/></svg>Regardless of age</li><br>
    <li><svg class="tick" viewBox="0 0 10 10"><circle cx="5" cy="5" r="5" fill="#fff"/><path d="M2.6 5.2l1.6 1.6 3.2-3.4" stroke="#97c157" stroke-width="1.4" fill="none"/></svg>for over a century</li>
    <li><svg class="tick" viewBox="0 0 10 10"><circle cx="5" cy="5" r="5" fill="#fff"/><path d="M2.6 5.2l1.6 1.6 3.2-3.4" stroke="#97c157" stroke-width="1.4" fill="none"/></svg>Naturally</li>
  </ul>
</section>

<section class="card card-front" aria-label="Card front">
  <div class="front-logo">
    <div class="brand-name">Bright Path Wellness</div>
    <div class="brand-rule"><span></span><b>CENTRE</b><span></span></div>
  </div>
  <div class="front-band">
    <div class="practitioner">
      <div class="practitioner-name">Dr. Marten Quogue</div>
      <div class="practitioner-cred">B.Sc., D.C.</div>
      <div class="practitioner-title">Chiropractor</div>
    </div>
    <div class="divider"></div>
    <div class="contact">
      <div>217 Tamsey Road</div>
      <div>Etobicoke ON. K2R 6P4</div>
      <div class="contact-row"><svg class="icon" viewBox="0 0 10 10"><path d="M2 1l2 2-1 1.2c.6 1.2 1.6 2.2 2.8 2.8L7 6l2 2-1.2 1.4C4.5 9 1 5.5.6 2.2z" fill="#fff"/></svg>416-870-2961 (MOVE)</div>
      <div class="contact-row"><svg class="icon" viewBox="0 0 10 10"><rect x="0.5" y="2" width="9" height="6.5" fill="#fff"/><path d="M.5 2l4.5 3.6L9.5 2" stroke="#97c157" fill="none"/></svg>brightpathchiro@mailnest.example</div>
      <div class="contact-row"><svg class="icon" viewBox="0 0 10 10"><circle cx="5" cy="5" r="4.5" fill="#fff"/><path d="M.5 5h9M5 .5c-2 2.5-2 6.5 0 9M5 .5c2 2.5 2 6.5 0 9" stroke="#97c157" stroke-width=".8" fill="none"/></svg>www.brightpathwellcentre.example</div>
    </div>
  </div>
</section>

</body>
</html>
```